Create company sales sheet to increase referrals so we can get new products

Create a 1 page sales sheet based on the text and logo that we provided.

We are a distribution company. Product manufacturer are a great source of leads for us - as they talk to our potential clients, eg., owners of medical projects, and we are hoping to get referrals.

Keep equal emphasis on each of the trhee words of "Clinical Supply Alliance.

Target Market(s)

Manufacturers of medical products

Industry/Entity Type

It Company

Requirements
Must have
• Equal emphasis on "Clinical Supply Alliance"
Nice to have
• We are expecting a one page one side, but if it looks better, you can make it go to a second page (or double sided)

```html
<!DOCTYPE html>
<html lang="en">
<head>
<meta charset="utf-8">
<title>Clinical Supply Alliance – Sales Sheet</title>
<link rel="stylesheet" href="https://fonts.googleapis.com/css2?family=Montserrat:wght@500;700&family=Lato:wght@400;700&family=Questrial&family=Oswald:wght@500;600&family=Roboto+Condensed:wght@700&display=swap">
<style>
  :root {
    --red: #c4161c;
    --red-dark: #8e0f13;
    --ink: #1b1b1b;
    --text: #2a2a2a;
    --panel: #eeeeee;
    --white: #ffffff;
    --black: #111111;
    --sky: #bfe3f7;
    --sky-deep: #5fb6e6;
  }
  * { margin: 0; padding: 0; box-sizing: border-box; }
  html, body { width: 900px; height: 1200px; overflow: hidden; background: var(--white); }
  .sheet { position: relative; width: 900px; height: 1200px; overflow: hidden; background: var(--white); font-family: "Lato", sans-serif; color: var(--text); }
  .art { position: absolute; left: 0; top: 0; }

  .brand { position: absolute; left: 36px; top: 52px; width: 370px; text-align: center; }
  .brand-dot { display: block; width: 58px; height: 58px; border-radius: 50%; background: var(--red); margin: 0 auto 14px; }
  .brand-name { font-family: "Montserrat", sans-serif; font-weight: 700; font-size: 25px; letter-spacing: 0.5px; color: var(--ink); white-space: nowrap; }

  .headline { position: absolute; left: 38px; top: 218px; font-family: "Montserrat", sans-serif; line-height: 1; }
  .headline .l1 { display: block; font-weight: 700; font-size: 33px; color: var(--ink); }
  .headline .l2 { display: block; font-weight: 500; font-size: 37px; color: var(--red); margin-top: 4px; letter-spacing: -0.5px; }
  .headline .l3 { display: block; font-weight: 500; font-size: 26px; color: var(--ink); margin-top: 6px; }

  .left-col { position: absolute; left: 0; top: 520px; width: 422px; height: 510px; background: linear-gradient(90deg, #f4f4f4, #e6e6e6); }
  .bar { position: absolute; left: 0; width: 422px; background: linear-gradient(180deg, var(--red), var(--red-dark)); color: var(--white); font-family: "Montserrat", sans-serif; font-weight: 700; font-size: 15px; text-align: center; line-height: 20px; display: flex; align-items: center; justify-content: center; }
  .copy { position: absolute; left: 36px; width: 362px; font-size: 13.4px; line-height: 17px; text-align: justify; }

  .questions { position: absolute; left: 460px; top: 545px; width: 420px; font-family: "Lato", sans-serif; font-size: 17px; line-height: 21px; color: var(--ink); }
  .questions p { margin-bottom: 10px; }
  .questions b { font-weight: 700; font-size: 19px; }
  .help { position: absolute; left: 440px; top: 676px; width: 440px; text-align: center; font-family: "Questrial", sans-serif; font-weight: 400; line-height: 1; }
  .help .h1 { display: block; font-size: 30px; color: var(--ink); letter-spacing: -0.3px; }
  .help .h2 { display: block; font-size: 44px; color: var(--red); margin-top: 6px; letter-spacing: 1px; }
  .pitch { position: absolute; left: 460px; top: 780px; width: 410px; font-size: 13.4px; line-height: 17px; text-align: justify; }
  .cta { position: absolute; left: 450px; top: 928px; width: 420px; text-align: center; font-family: "Roboto Condensed", sans-serif; font-weight: 700; font-size: 18px; line-height: 24px; color: var(--ink); }

  .footer { position: absolute; left: 0; top: 1070px; width: 900px; text-align: center; color: var(--white); }
  .phone { font-family: "Oswald", sans-serif; font-weight: 600; font-size: 34px; display: inline-flex; align-items: center; gap: 10px; }
  .web, .addr { font-size: 15px; display: flex; align-items: center; justify-content: center; gap: 8px; }
  .web { font-size: 17px; margin-top: 4px; }
  .addr { font-size: 13.5px; margin-top: 6px; }
</style>
</head>
<body>
<main class="sheet">
  <svg class="art" width="900" height="1200" viewBox="0 0 900 1200" aria-hidden="true">
    <defs>
      <linearGradient id="heroTone" x1="0" y1="0" x2="1" y2="0">
        <stop offset="0" stop-color="#ffffff"/>
        <stop offset="0.35" stop-color="#e6f3fb"/>
        <stop offset="1" stop-color="#9fd3f1"/>
      </linearGradient>
    </defs>
    <path d="M0 0 H900 V20 C700 8 500 -2 0 40 Z" fill="var(--black)"/>
    <path d="M0 40 C500 -2 700 8 900 20 V34 C700 22 480 14 0 56 Z" fill="var(--red)"/>
    <path d="M0 56 C480 14 700 22 900 34 V520 H0 Z" fill="#ffffff"/>
    <path d="M230 130 C420 80 700 110 900 100 V500 H230 Z" fill="url(#heroTone)" role="img" aria-label="Medical care concept: hand presenting glowing hexagon health icons"/>
    <path d="M0 390 C180 470 480 500 900 470 V520 H0 Z" fill="var(--black)"/>
    <path d="M0 412 C200 486 500 512 900 490 V520 H0 Z" fill="var(--red)"/>
    <path d="M0 428 C220 500 520 522 900 506 V520 H0 Z" fill="#ffffff"/>
    <path d="M0 1030 C300 1010 600 1010 900 1045 V1200 H0 Z" fill="var(--red)"/>
    <path d="M0 1048 C300 1028 600 1028 900 1062 V1200 H0 Z" fill="var(--black)"/>
  </svg>

  <div class="brand">
    <span class="brand-dot"></span>
    <div class="brand-name">CLINICAL SUPPLY ALLIANCE</div>
  </div>

  <h1 class="headline">
    <span class="l1">WE GIVE NEW</span>
    <span class="l2">MEDICAL PRODUCT</span>
    <span class="l3">INNOVATORS A CHANCE</span>
  </h1>

  <section class="left-col">
    <h2 class="bar" style="top:16px;height:44px;">GROW YOUR MANUFACTURING ENTERPRISE<br>INTO A MANUFACTURING POWERHOUSE</h2>
    <p class="copy" style="top:86px;">Enlighten your customers about CSA and increase manufacturing volumes, as well as earning customer appreciation, loyalty, and referrals.</p>
    <h2 class="bar" style="top:162px;height:28px;">OUR FOCUS</h2>
    <p class="copy" style="top:214px;">We are especially interested in technologies that improve patient care, prevent injury or illness, reduce or mitigate disabilities, save lives, and/or decreases healthcare costs. We look for technologies supported by clinical studies and evidence-based practices.</p>
    <h2 class="bar" style="top:318px;height:46px;">DISTRIBUTION AND<br>PRODUCT LAUNCH SUPPORT</h2>
    <p class="copy" style="top:390px;">CSA handles all aspects of distribution, product launch, marketing, and sales. We execute creative and effective product launch strategies, using customer motivation psychology combined with targeted and comprehensive client materials, experienced sales force, and extensive global distribution channels.</p>
  </section>

  <div class="questions">
    <p><b>D</b>o you have effective products with<br>low sales numbers in need of a distribution partner?</p>
    <p><b>D</b>o you have customers with innovative products<br>that need distribution services?</p>
  </div>

  <h2 class="help">
    <span class="h1">CLINICAL SUPPLY ALLIANCE</span>
    <span class="h2">CAN HELP!</span>
  </h2>

  <p class="pitch">Increase your production volume by assisting your customers with product distribution. We will distribute your customers' promising new products with strategic launch analysis, comprehensive targeted marketing programs, and global fulfillment and distribution services, at no cost to manufacturers. Clinical Supply Alliance (CSA) specializes in launching new medical products by partnering with medical innovators in bringing new and next generation medical technologies to market.</p>

  <p class="cta">ASSIST YOUR CLIENTS AND<br>INCREASE YOUR MANUFACTURING VOLUME<br>AND PROFITS</p>

  <footer class="footer">
    <div class="phone">
      <svg width="22" height="22" viewBox="0 0 24 24" aria-hidden="true"><circle cx="12" cy="12" r="12" fill="var(--red)"/><path d="M8 6c1 0 1.6 2 1.6 2.6 0 .6-.9 1-.9 1.6.4 1.4 2 3 3.4 3.4.6 0 1-.9 1.6-.9.6 0 2.6.6 2.6 1.6 0 1-1.2 2-2.2 2C10 18.3 5.7 14 5.7 8.2 5.7 7.2 7 6 8 6z" fill="#fff"/></svg>
      555-014-2290
    </div>
    <div class="web">
      <svg width="14" height="11" viewBox="0 0 14 11" aria-hidden="true"><rect width="14" height="11" rx="2" fill="var(--red)"/><path d="M1 2l6 4 6-4" stroke="#fff" stroke-width="1.4" fill="none"/></svg>
      www.clinicalsupplyalliance.example
    </div>
    <div class="addr">
      <svg width="10" height="14" viewBox="0 0 10 14" aria-hidden="true"><path d="M5 0a5 5 0 0 1 5 5c0 3.5-5 9-5 9S0 8.5 0 5a5 5 0 0 1 5-5z" fill="#fff"/><circle cx="5" cy="5" r="1.8" fill="var(--black)"/></svg>
      Clinical Supply Alliance, 4820 Harbor Lane, Dover, DE 19901
    </div>
  </footer>
</main>
</body>
</html>
```